Bright Lantern Studios Business Card Design

Doug Farley

Managing Partner

Doug@BrightLanternStudios.com

BrightLanternStudios.com

502-417-2356

Industry/Entity Type

Photographer

Contact Information for Business Card

Doug Farley

Managing Partner

Doug@BrightLanternStudios.com

BrightLanternStudios.com

502-417-2356

Requirements
Must have
• Must show that I am a pavlo trusted photographer

```html
<!DOCTYPE html>
<html lang="en">
<head>
<meta charset="utf-8">
<title>Bright Lantern Studios – Business Card</title>
<link rel="stylesheet" href="https://fonts.googleapis.com/css2?family=Josefin+Sans:wght@400;600&family=Lato:wght@400&display=swap">
<style>
  :root {
    --backdrop: #2b2725;
    --card-white: #ffffff;
    --card-black: #0b0b0b;
    --ink: #111111;
    --paper-text: #ffffff;
    --badge-amber: #f2b233;
    --muted: #d8d8d8;
  }
  * { margin: 0; padding: 0; box-sizing: border-box; }
  html, body { width: 1200px; height: 780px; overflow: hidden; }
  body {
    background: var(--backdrop);
    position: relative;
    font-family: "Lato", sans-serif;
  }
  .card {
    position: absolute;
    top: 238px;
    width: 530px;
    height: 303px;
    overflow: hidden;
  }

  /* Front */
  .card-front { left: 40px; background: var(--card-white); }
  .front-mark {
    position: absolute; left: 50%; top: 62px;
    width: 52px; height: 52px; margin-left: -26px;
    border-radius: 50%; background: var(--ink);
  }
  .front-name {
    position: absolute; left: 0; right: 0; top: 132px;
    text-align: center;
    font-family: "Josefin Sans", sans-serif; font-weight: 600;
    font-size: 25px; letter-spacing: 1px; text-transform: uppercase;
    color: var(--ink);
  }
  .trusted-badge {
    position: absolute; left: 50%; top: 186px;
    width: 96px; height: 30px; margin-left: -48px;
    border-radius: 6px; background: var(--badge-amber);
  }

  /* Back */
  .card-back { left: 630px; background: var(--card-black); }
  .back-band {
    position: absolute; left: 0; right: 0; top: 42px; height: 78px;
    background: var(--card-white);
  }
  .back-mark {
    position: absolute; left: 300px; top: 66px;
    width: 108px; height: 108px; border-radius: 50%;
    background: var(--card-black);
  }
  .back-name {
    position: absolute; left: 60px; right: 20px; top: 186px;
    font-family: "Josefin Sans", sans-serif; font-weight: 600;
    font-size: 25px; letter-spacing: 1px; text-transform: uppercase;
    color: var(--paper-text);
  }
  .person {
    position: absolute; right: 325px; top: 235px;
    text-align: right; color: var(--paper-text);
    font-family: "Josefin Sans", sans-serif;
  }
  .person-name { font-size: 15px; text-transform: uppercase; }
  .person-title { font-size: 13px; color: var(--muted); }
  .divider {
    position: absolute; left: 217px; top: 228px;
    width: 1px; height: 58px; background: var(--paper-text);
  }
  .contact-list {
    position: absolute; left: 232px; top: 228px;
    list-style: none; color: var(--paper-text); font-size: 13px;
  }
  .contact-list li { display: flex; align-items: center; gap: 7px; height: 20px; }
  .contact-list svg { width: 14px; height: 14px; flex: none; }
</style>
</head>
<body>
  <section class="card card-front" aria-label="Card front">
    <div class="front-mark"></div>
    <h1 class="front-name">Bright Lantern Studios</h1>
    <div class="trusted-badge" role="img" aria-label="Trusted photographer listing badge"></div>
  </section>

  <section class="card card-back" aria-label="Card back">
    <div class="back-band"></div>
    <div class="back-mark"></div>
    <h2 class="back-name">Bright Lantern Studios</h2>

    <div class="person">
      <p class="person-name">Doug Farley</p>
      <p class="person-title">Managing Partner</p>
    </div>
    <div class="divider"></div>

    <ul class="contact-list">
      <li>
        <svg viewBox="0 0 14 14" aria-hidden="true"><circle cx="7" cy="7" r="6.3" fill="none" stroke="#fff" stroke-width="1.2"/><path d="M4.5 4.2h1.6l.6 1.6-.9.7a4 4 0 0 0 1.7 1.7l.7-.9 1.6.6v1.6c-3 .3-5.6-2.3-5.3-5.3z" fill="#fff"/></svg>
        502-417-2356
      </li>
      <li>
        <svg viewBox="0 0 14 14" aria-hidden="true"><circle cx="7" cy="7" r="6.3" fill="none" stroke="#fff" stroke-width="1.2"/><rect x="3.8" y="4.8" width="6.4" height="4.4" fill="none" stroke="#fff" stroke-width="1"/><path d="M3.8 4.8 7 7.4l3.2-2.6" fill="none" stroke="#fff" stroke-width="1"/></svg>
        Doug@BrightLanternStudios.com
      </li>
      <li>
        <svg viewBox="0 0 14 14" aria-hidden="true"><circle cx="7" cy="7" r="6.3" fill="none" stroke="#fff" stroke-width="1.2"/><circle cx="7" cy="7" r="3.4" fill="none" stroke="#fff" stroke-width="0.9"/><path d="M3.6 7h6.8M7 3.6v6.8" stroke="#fff" stroke-width="0.9"/></svg>
        BrightLanternStudios.com
      </li>
    </ul>
  </section>
</body>
</html>
```